Design for schnapps bottle label "El Sendero"

Hi! On a small land lot we are producing our own Italian schnapps "Grappa". For the bottles we would like to modernize our current labes that you find below. The two cats looking at each other should remain, but updated and more modern. I am very much looking forward to your suggestions. Best, Tobias

Target Market(s)

Schnapps bottle label

Requirements
Must have
• Cats should resemble the cats that are decorating the house entry (see attached), however, should have a more modern appearance.

Text elements should remain: "Grappa", "El Sendero", "Legnoso", "[Vintage Year], "Raccolta No", "Vol %"
Should not have
• Current ornament can be used, replaced or deleted (whatever looks best)

```html
<!DOCTYPE html>
<html lang="en">
<head>
<meta charset="utf-8">
<title>El Sendero Grappa – Bottle Label</title>
<link rel="stylesheet" href="https://fonts.googleapis.com/css2?family=Allura&family=Cormorant+Garamond:wght@500;600&display=swap">
<style>
  :root {
    --page-bg: #e2e2e2;
    --label-paper: #fce8d0;
    --ink: #111111;
    --ink-inverse: #fce8d0;
    --illustration-tone: #1a1a1a;
    --illustration-fade: #3a3a3a;
  }
  * { box-sizing: border-box; margin: 0; padding: 0; }
  html, body {
    width: 838px;
    height: 1200px;
    overflow: hidden;
    background: var(--page-bg);
  }
  .canvas {
    position: relative;
    width: 838px;
    height: 1200px;
  }
  .label {
    position: absolute;
    left: 171px;
    width: 495px;
    background: var(--label-paper);
    color: var(--ink);
    font-family: "Cormorant Garamond", "Times New Roman", serif;
  }
  .label--main {
    top: 94px;
    height: 795px;
  }
  .label--maker {
    top: 931px;
    height: 175px;
    display: flex;
    align-items: center;
    justify-content: center;
  }
  .product-name {
    position: absolute;
    top: 68px;
    left: 0;
    width: 100%;
    text-align: center;
    font-size: 84px;
    font-weight: 500;
    letter-spacing: 6px;
    line-height: 1;
  }
  .cats-illustration {
    position: absolute;
    left: 51px;
    top: 232px;
    width: 390px;
    height: 165px;
  }
  .variety-band {
    position: absolute;
    left: 84px;
    top: 487px;
    width: 327px;
    height: 48px;
    background: var(--ink);
    color: var(--ink-inverse);
    display: flex;
    align-items: center;
    justify-content: center;
    font-size: 30px;
    font-weight: 500;
    letter-spacing: 3px;
  }
  .details {
    position: absolute;
    top: 628px;
    left: 0;
    width: 100%;
    text-align: center;
    font-size: 33px;
    font-weight: 500;
    letter-spacing: 2px;
    line-height: 52px;
  }
  .details .spacer { display: inline-block; width: 16px; }
  .maker-name {
    font-family: "Allura", cursive;
    font-size: 76px;
    line-height: 1;
    transform: translateY(4px);
  }
</style>
</head>
<body>
  <main class="canvas">
    <section class="label label--main">
      <h1 class="product-name">GRAPPA</h1>
      <svg class="cats-illustration" viewBox="0 0 390 165" role="img" aria-label="Illustration of two black cats stretching and facing each other">
        <defs>
          <radialGradient id="cats-tone" cx="50%" cy="60%" r="60%">
            <stop offset="0%" stop-color="var(--illustration-fade)" stop-opacity="0.35"/>
            <stop offset="100%" stop-color="var(--illustration-tone)" stop-opacity="0.18"/>
          </radialGradient>
        </defs>
        <rect x="0" y="0" width="390" height="165" rx="6" fill="url(#cats-tone)"/>
      </svg>
      <div class="variety-band">LEGNOSO 2015</div>
      <p class="details">
        RACCOLTA NO.01<br>
        41.0% VOL.<span class="spacer"></span>70 CL
      </p>
    </section>
    <section class="label label--maker">
      <p class="maker-name">El Sendero</p>
    </section>
  </main>
</body>
</html>
```